Banner Ad Design Project

I need a banner design. The website is under construction at www.brightmarrow.example

Name: Bright Marrow
Tagline: Steady Sparks for crowded calendars

This is a leadership development and executive coaching site. The past site is live at www.quillstepnow.example. (so you can get a sense of the content)

The audience are (BUSY) executives, senior managers, leaders and top professionals, so the feel needs to be highly professional but also modern and fresh. I want to communicate energy but also solid and trust worthy and not too new agey. The audience are also people with strong social values who want to change things - so not too corporate (Ie suits!)

I would like the design to be floating on a white background, very clean and simple. I am attracted to reds or sunset (burn orange crimson colors.) But totally open to any color ideas.
I am giving an open brief for your ideas.
Here are the dimensions 960px wide, roughly 190px height.

Reason: The weekend might give more time to designers to get involved. Thanks Vina

Hi designers

You may not have seen the additions I gave to this brief.

The banner should not have leader out front photo's. Maybe less corporate than I initially thought. 
Not too corporate (no suits!) Please no chess pieces, jigsaw pieces, cartoon images, cliche leadership images. 
Am am trying for inspiration /inspiring whilst still being professional. Very simple and clean.
Please can the design be floating in a white background so that the web page is borderless - A bit like it is in http://palmoriskel.example/
Thank you

Target Market(s)

Senior managers, executives but people who also want to change the world!

Industry/Entity Type

Construction

Requirements
Should not have
• Should not have leader out front photo's.
Maybe less corporate than I initially thought.
Am am trying for inspiration /inspiring whilst still being professional.
Please no chess pieces, jigsaw pieces, cartoon images, cliche leadership images. Not too corporate (Ie suits!)

Thanks

```html
<!DOCTYPE html>
<html lang="en">
<head>
<meta charset="utf-8">
<title>Bright Marrow — Banner</title>
<link rel="stylesheet" href="https://fonts.googleapis.com/css2?family=Roboto:wght@300&display=swap">
<style>
  :root {
    --canvas-grey: #e3e1dd;
    --canvas-light: #ecebe8;
    --glow-yellow: #f6ec2a;
    --glow-soft: rgba(246, 236, 42, 0);
    --ink: #161616;
    --ember-red: #c9453f;
    --tagline-red: #e0504a;
    --match-wood: #e8cf9e;
    --match-head: #d42a2a;
  }
  html, body {
    margin: 0;
    padding: 0;
    overflow: hidden;
  }
  .banner {
    position: relative;
    width: 1200px;
    height: 238px;
    overflow: hidden;
    font-family: "Roboto", "Helvetica Neue", Arial, sans-serif;
    font-weight: 300;
    background:
      radial-gradient(ellipse 150px 150px at 535px 70px, var(--glow-yellow), var(--glow-soft) 100%),
      radial-gradient(ellipse 150px 150px at 690px 70px, var(--glow-yellow), var(--glow-soft) 100%),
      radial-gradient(ellipse 260px 200px at 610px 60px, rgba(246, 236, 42, 0.55), var(--glow-soft) 100%),
      linear-gradient(90deg, var(--canvas-grey) 0%, var(--canvas-light) 100%);
  }
  .brand-name {
    position: absolute;
    left: 0;
    top: 0;
    margin: 0;
    font-weight: 300;
    color: var(--ink);
    font-size: 84px;
    line-height: 1;
    letter-spacing: -2px;
  }
  .brand-name__line {
    position: absolute;
    white-space: nowrap;
  }
  .brand-name__line--first {
    left: 33px;
    top: 34px;
  }
  .brand-name__line--second {
    left: 83px;
    top: 114px;
  }
  .matches-photo {
    position: absolute;
    left: 400px;
    top: 14px;
    width: 436px;
    height: 224px;
    background: linear-gradient(180deg,
      rgba(232, 207, 158, 0) 0%,
      rgba(232, 207, 158, 0.35) 50%,
      var(--match-head) 68%,
      #b51f22 80%,
      var(--match-wood) 100%);
  }
  .tagline {
    position: absolute;
    left: 852px;
    top: 194px;
    margin: 0;
    font-size: 14px;
    font-weight: 300;
    color: var(--tagline-red);
    white-space: nowrap;
  }
</style>
</head>
<body>
  <header class="banner">
    <h1 class="brand-name">
      <span class="brand-name__line brand-name__line--first">Bright</span>
      <span class="brand-name__line brand-name__line--second">Marrow</span>
    </h1>
    <div class="matches-photo" role="img" aria-label="Photograph of a row of red-tipped matches with one taller green-tipped match standing above them, lit by a yellow glow"></div>
    <p class="tagline">Steady Sparks for crowded calendars</p>
  </header>
</body>
</html>
```